Speisekarten-Design für italienisches Restaurant im Golfclub mit Blick auf die Alpen
Zielgruppe
Italienisches Restaurant im Golfclub mit Blick auf die Alpen (bei gutem Wetter)
Aufgabenstellung
Karte muss weiterhin bearbeitet werden könne. Es geht um ein Design das optisch anspricht aber nicht übertrieben ist. Die Blätter kommen später in eine Menukarte die noch in Auftrag gegeben werden.
Im Idealfall kann der Designer hierfür auch was mit designen das an einen Firma weitergeben werden kann um die 'Umschläge zu erstellen. Logo kann muss nicht mit drin sein. Es geht auch sehr um die einfache Darstellung des Ganzen.

```html
<!DOCTYPE html>
<html lang="de">
<head>
<meta charset="utf-8">
<title>Ristorante Solvento – Menüs</title>
<link href="https://fonts.googleapis.com/css2?family=Arimo:wght@400&family=Roboto+Condensed:wght@700&display=swap" rel="stylesheet">
<style>
  :root {
    --ink: #3f3f41;
    --header: #221f1e;
    --gold: #c9a24a;
    --sand: #bfb29a;
    --rule: #c7bba3;
    --paper: #ffffff;
    --footer: #434244;
  }
  * { margin: 0; padding: 0; box-sizing: border-box; }
  html, body { width: 735px; height: 1200px; overflow: hidden; background: var(--paper); }
  .menu-card { position: relative; width: 735px; height: 1200px; background: var(--paper); font-family: "Arimo", Arial, sans-serif; color: var(--ink); }

  .masthead { position: absolute; left: 0; top: 0; width: 735px; height: 150px; background: var(--header); }
  .brand { position: absolute; left: 0; width: 735px; text-align: center; color: var(--gold); font-family: "Arimo", Arial, sans-serif; font-weight: 400; }
  .brand-kicker { top: 53px; font-size: 10px; letter-spacing: 6px; }
  .brand-name { top: 74px; font-size: 40px; letter-spacing: 1px; line-height: 46px; }
  .brand-sub { top: 121px; font-size: 7px; letter-spacing: 4px; }

  .rule { position: absolute; left: 85px; width: 580px; height: 1px; background: var(--rule); }

  .menu-title { position: absolute; left: 85px; font-family: "Roboto Condensed", "Arial Narrow", sans-serif; font-weight: 700; font-size: 53px; line-height: 50px; letter-spacing: -1px; color: var(--ink); transform: scaleX(0.88); transform-origin: left center; }

  .course-list { position: absolute; left: 85px; width: 400px; list-style: none; font-size: 13px; line-height: 16px; }
  .course-list li { margin-bottom: 15.6px; }

  .price-tag { position: absolute; left: 498px; width: 168px; height: 166px; background: var(--sand); display: flex; align-items: center; justify-content: center; font-family: "Roboto Condensed", "Arial Narrow", sans-serif; font-weight: 700; font-size: 48px; color: var(--ink); }

  .produce-art { position: absolute; left: 20px; top: 956px; width: 675px; height: 205px; background: radial-gradient(ellipse at center, #e4e4e4 0%, #f3f3f3 60%, #ffffff 100%); }
  .footer-bar { position: absolute; left: 166px; top: 1170px; width: 403px; height: 30px; background: var(--footer); }
</style>
</head>
<body>
<main class="menu-card">
  <header class="masthead">
    <div class="brand brand-kicker">RISTORANTE</div>
    <div class="brand brand-name">SOLVENTO</div>
    <div class="brand brand-sub">IM GOLFCLUB HOHE LANZ</div>
  </header>

  <div class="rule" style="top:224px"></div>

  <h2 class="menu-title" style="top:262px">MENU 1</h2>
  <ul class="course-list" style="top:322px">
    <li>Appetithäppchen und Aperitif</li>
    <li>Italiensicher Aufschnitt Teller</li>
    <li>Pasta mit Hackfleischsoße und Sahne</li>
    <li>Kalbsbraten mit Barolosoße und Rosmarin Kartoffeln</li>
    <li>Zitronen Sorbet</li>
  </ul>
  <div class="price-tag" style="top:240px">49,-</div>

  <div class="rule" style="top:481px"></div>

  <h2 class="menu-title" style="top:515px">MENU 2</h2>
  <ul class="course-list" style="top:577px">
    <li>Gemischter Salat</li>
    <li>Pasta mit scharfer Tomatensoße</li>
    <li>Putengeschnetzeltes in Currysoße mit Reis</li>
    <li>Tiramisu</li>
  </ul>
  <div class="price-tag" style="top:495px">35,-</div>

  <div class="rule" style="top:701px"></div>

  <h2 class="menu-title" style="top:729px">MENU 3</h2>
  <ul class="course-list" style="top:785px">
    <li>Aperitif</li>
    <li>Vitello Tonnato</li>
    <li>Lasagne im Ofen überbacken</li>
    <li>Rumpsteak tranchiert, auf Rucola Bett serviert mit<br>gehobelten Original Parmesan Käse</li>
    <li>Rosmarinkartoffeln und Gemüse</li>
    <li>Panna Cotta mit Waldfrüchte</li>
  </ul>
  <div class="price-tag" style="top:719px">55,-</div>

  <div class="produce-art" role="img" aria-label="Gezeichnete Gemüse-Illustration: Paprika, Zwiebeln, Knoblauch, Chilischoten, Karotten, Erbsenschoten und Auberginen"></div>
  <div class="footer-bar"></div>
</main>
</body>
</html>
```